Cedar Lantern Gazette Website Redesign to Better Access Local News and distribute it to more people

I currently have the local news website www.cedarlanterngazette.com and am seeking a new front page design that will update the main page and make it more current and user friendly, including ways to post to the sight from my cell phone, connectivity to friendloop, chirpwave, and snapmosaic accounts and other updates to provide clients with a "new face" and updated way of getting their news. It's been approximately 10 years since I've updated the main page and I know that it needs a fresh new look.

I'm a professional photographer, thus I want to highlight my photography work on a daily basis and offer photographs for the public to enjoy, as this has been a "drawing point" over other local media outlets.

The website is locally know for providing numerous photos of local news events and giving the public access to seeing themselves in the news.

You can also access my friendloop page cedarlantern gazette and see additional content that I provide there for over 17000 friends and followers.

I want a way to archive old material, for future access, but to "cut down" on the clutter of the page.

I also want to keep the way that I can sell advertising at the current ad levels but would also like to sell additional space on the sides of the front page, for increase revenue.

I currently update the website with vellum-works composer, daily.

I have some ideas in mind, but am open to new and fresh ideas and ways to make it more user friendly. If you have any questions, please message me and I'll try to explain more fully.

Target Market(s)

Public as a news source

Industry/Entity Type

News

Coding

Coded - Design and coding required

Number of Pages Required

1 page

Font styles to use
Sans Serif

Requirements
Must have
• Ways to upload material from friendloop, a way to post three photos each day that are changed out daily and ways to automatically archive old material. Must look good on cell phones.
Nice to have
• Anything that would streamline news feed and make it easier accessible to other media.
Should not have
• Open.

```html
<!DOCTYPE html>
<html lang="en">
<head>
<meta charset="utf-8">
<title>Cedar Lantern Gazette</title>
<link href="https://fonts.googleapis.com/css2?family=Open+Sans:wght@400;600;700&family=Roboto+Slab:wght@700&display=swap" rel="stylesheet">
<style>
:root{
  --red:#c8171e;
  --red-dark:#a50f15;
  --ink:#222;
  --text:#555;
  --muted:#999;
  --rule:#e2e2e2;
  --bar:#1f1f1f;
  --footer:#1c1c1c;
  --white:#fff;
}
*{box-sizing:border-box;margin:0;padding:0}
html,body{width:1200px;height:2836px;overflow:hidden}
body{position:relative;background:var(--white);font-family:"Open Sans",Arial,sans-serif;color:var(--text);font-size:11px;line-height:1.45}
.abs{position:absolute}
.ph{display:block}

/* top bar */
.topbar{left:0;top:0;width:1200px;height:32px;background:var(--bar);color:#ddd;font-size:11px;display:flex;align-items:center;justify-content:space-between;padding:0 80px}
.flash b{color:var(--white)}
.top-social{display:flex;gap:10px}
.top-social span{width:12px;height:12px;border-radius:50%;background:#777;display:block}

/* header */
.brand{left:80px;top:44px;display:flex;align-items:center;gap:10px;font-weight:700;font-size:20px;color:var(--red)}
.brand i{width:16px;height:16px;background:var(--red);display:block}
.banner-ad{left:560px;top:38px;width:580px;height:72px;background:linear-gradient(90deg,#0e2d5b,#1d5a9a 55%,#0b2244)}

/* nav */
.nav{left:0;top:116px;width:1200px;height:36px;background:var(--red);display:flex;align-items:center;padding:0 80px;color:var(--white);font-size:12px;font-weight:600}
.nav a{color:inherit;text-decoration:none;margin-right:38px}
.nav .home{background:var(--red-dark);padding:10px 14px;margin-right:24px}
.nav .account{margin-left:auto;display:flex;gap:30px}
.nav .account a{margin:0}

/* slider */
.slider{left:80px;top:176px;width:500px;height:420px;background:linear-gradient(135deg,#cfd6db,#7f8b93 60%,#4a545b)}
.slider .caption{position:absolute;left:0;bottom:0;width:100%;padding:14px 16px 26px;background:rgba(0,0,0,.55);color:var(--white)}
.caption h3{font-size:15px;font-weight:700;margin-bottom:4px}
.caption p{font-size:10px;color:#ddd}
.dots{position:absolute;left:50%;bottom:8px;transform:translateX(-50%);display:flex;gap:6px}
.dots span{width:8px;height:8px;background:#bbb}
.dots span:first-child{background:var(--white)}

/* tabs */
.tabs{left:600px;top:176px;width:220px}
.tab-buttons{display:flex;gap:4px;margin-bottom:10px}
.tab-buttons span{font-size:10px;padding:4px 10px;border:1px solid var(--rule);color:var(--ink)}
.tab-buttons .on{background:#555;color:var(--white);border-color:#555}
.tab-item{border-bottom:1px solid var(--rule);padding:8px 0;height:78px}
.tab-item h4{font-size:11px;color:var(--ink);font-weight:700}
.meta{font-size:9px;color:var(--muted);margin:2px 0}
.tab-item p{font-size:9.5px}

/* sections */
.section-title{font-family:"Roboto Slab",Georgia,serif;font-size:20px;color:var(--ink);border-bottom:2px solid var(--rule);padding-bottom:8px;width:740px;left:80px}
.section-title::after{content:"";position:absolute;left:0;bottom:-2px;width:110px;height:2px;background:var(--red)}
.arrows{position:absolute;right:0;top:4px;font-size:16px;color:var(--ink);letter-spacing:8px}
.cards{left:80px;width:740px;display:grid;grid-template-columns:repeat(4,1fr);gap:20px}
.card .ph{height:180px}
.card h4{font-size:11px;color:var(--ink);margin-top:10px}
.card p{font-size:9.5px}

.travel{left:80px;width:740px}
.story{display:flex;gap:20px;height:240px;border-bottom:1px solid var(--rule);padding-top:20px}
.story .ph{width:240px;height:200px;flex:none}
.story h3{font-size:14px;color:var(--ink);font-weight:700}
.story p{font-size:10.5px;margin-top:10px}

.ad-strip{left:80px;top:1910px;width:740px;display:grid;grid-template-columns:repeat(5,1fr);gap:14px}
.ad-strip .ph{height:210px}

/* side column */
.side{left:872px;width:248px}
.newsletter{left:872px;top:1572px;width:248px;height:200px;background:var(--bar);color:#ccc;padding:18px}
.newsletter h4{color:var(--white);font-size:13px;letter-spacing:1px;margin-bottom:10px}
.newsletter p{font-size:10px;margin-bottom:14px}
.nl-form{display:flex}
.nl-form span{flex:1;height:30px;background:var(--white)}
.nl-form b{width:40px;height:30px;background:var(--red)}

/* footer */
.footer{left:0;top:2540px;width:1200px;height:296px;background:var(--footer);color:#ccc;font-size:11px;padding:40px 80px 0}
.foot-cols{display:grid;grid-template-columns:repeat(4,1fr);gap:40px}
.foot-cols li{list-style:none;margin-bottom:12px}
.foot-social li{display:flex;align-items:center;gap:8px}
.foot-social i{width:10px;height:10px;border-radius:50%;background:#888;display:block}
.copy{position:absolute;left:0;bottom:0;width:100%;text-align:center;border-top:1px solid #333;padding:14px 0;font-size:10px;color:#888}
</style>
</head>
<body>

<div class="abs topbar">
  <div class="flash"><b>Flash News :</b> In rhoncus nisa quam, a maximus tortor dapibus eget. Nullam iaculis, ex id ultricies condimentum.</div>
  <div class="top-social"><span></span><span></span><span></span><span></span></div>
</div>

<div class="abs brand"><i></i>Cedar Lantern Gazette</div>
<div class="abs banner-ad ph" role="img" aria-label="Banner advertisement for the Riverbend Fish Fry event"></div>

<nav class="abs nav">
  <a class="home">Home</a><a>News</a><a>Blog</a><a>Subscribe</a><a>Advertise</a><a>Contact</a>
  <div class="account"><a>Register</a><a>Login</a></div>
</nav>

<div class="abs slider" role="img" aria-label="Featured photo of colleagues meeting at an office table">
  <div class="caption">
    <h3>In rhoncus nisa quam</h3>
    <p>Sed faucibus est maximus eros congue. Mauris sagittis in erat et facilisi. Cras et risus efficitur tortor lobortis pulvinar.</p>
  </div>
  <div class="dots"><span></span><span></span><span></span><span></span></div>
</div>

<aside class="abs tabs">
  <div class="tab-buttons"><span class="on">Popular</span><span>Most Read</span></div>
  <div class="tab-item"><h4>In rhoncus nisa quam, a maximus</h4><div class="meta">June 12, 2024</div><p>Mauris sagittis in erat et facilisi. Cras et risus efficitur pulvinar.</p></div>
  <div class="tab-item"><h4>Sed faucibus est maximus eros congue</h4><div class="meta">June 11, 2024</div><p>Mauris sagittis in erat et facilisi. Cras et risus efficitur pulvinar.</p></div>
  <div class="tab-item"><h4>Magna vitae consequat dapibus</h4><div class="meta">June 10, 2024</div><p>Mauris sagittis in erat et facilisi. Cras et risus efficitur pulvinar.</p></div>
  <div class="tab-item"><h4>Sed faucibus est maximus eros congue</h4><div class="meta">June 09, 2024</div><p>Mauris sagittis in erat et facilisi. Cras et risus efficitur pulvinar.</p></div>
  <div class="tab-item"><h4>Sed faucibus est maximus eros congue</h4><div class="meta">June 08, 2024</div><p>Mauris sagittis in erat et facilisi. Cras et risus efficitur pulvinar.</p></div>
</aside>

<h2 class="abs section-title" style="top:668px">News Headlines<span class="arrows">‹›</span></h2>
<div class="abs cards" style="top:724px">
  <div class="card"><div class="ph" role="img" aria-label="Photo of a business meeting" style="background:linear-gradient(135deg,#d9dde0,#8a949b)"></div><h4>Sed faucibus est maximus eros congue</h4><p>Mauris sagittis in erat et facilisi. Cras et risus efficitur.</p></div>
  <div class="card"><div class="ph" role="img" aria-label="Photo of people working at laptops" style="background:linear-gradient(135deg,#c9b8a6,#6f5f52)"></div><h4>Magna vitae consequat dapibus</h4><p>Mauris sagittis in erat et facilisi. Cras et risus efficitur.</p></div>
  <div class="card"><div class="ph" role="img" aria-label="Photo of a team in discussion" style="background:linear-gradient(135deg,#e3e5e6,#9aa3a8)"></div><h4>Sed faucibus est maximus eros congue</h4><p>Mauris sagittis in erat et facilisi. Cras et risus efficitur.</p></div>
  <div class="card"><div class="ph" role="img" aria-label="Photo of an office group shaking hands" style="background:linear-gradient(135deg,#cdd3d8,#5e6a73)"></div><h4>Sed faucibus est maximus eros congue</h4><p>Mauris sagittis in erat et facilisi. Cras et risus efficitur.</p></div>
</div>

<h2 class="abs section-title" style="top:1040px">Travel News</h2>
<div class="abs travel" style="top:1090px">
  <article class="story"><div class="ph" role="img" aria-label="Photo of a city skyline" style="background:linear-gradient(180deg,#a9c3da,#5f7a92 70%,#3c4d5c)"></div>
    <div><h3>Phasellus eget velit vestibulum, facilisis lectus in.</h3><div class="meta">June 12, 2024 · 324 Views</div><p>In efficitur tellus ipsum, quis accumsan lacus vehicula nec. Fusce sapien nisi sit amet tristique accumsan. Curabitur sollicitudin, nisi sit amet consequat laoreet, erat est sollicitudin mauris, et tincidunt lorem tellus quis turpis. Sed a augue commodo, mollis leo ac, viverra odio. Etiam id pretium ex.</p></div></article>
  <article class="story"><div class="ph" role="img" aria-label="Photo of a road through red desert cliffs" style="background:linear-gradient(180deg,#9cc3e0,#c7784a 55%,#8a4b2c)"></div>
    <div><h3>Vestibulum ante ipsum primis in faucibus</h3><div class="meta">June 11, 2024 · 211 Views</div><p>Sed faucibus est maximus eros congue ullamcorper. Mauris sagittis in erat et facilisi. Cras et risus efficitur lorem pulvinar non nec ipsum. Morbi sodales lectus a tempus ullamcorper dapibus, massa libero maximus libero, vel vehicula nibh erat vel tellus. Ut non ullamcorper massa. Ut et nunc in libero porttitor interdum ut ac nisi. Cras bibendum, lorem ut dui.</p></div></article>
  <article class="story"><div class="ph" role="img" aria-label="Photo of a lakeside town at sunset" style="background:linear-gradient(180deg,#f2c27a,#b88c5c 50%,#5a5148)"></div>
    <div><h3>Suscipit ipsum tempor pretium pulvinar.</h3><div class="meta">June 10, 2024 · 198 Views</div><p>Phasellus eget velit vestibulum, facilisis lectus in, commodo lectus. In efficitur tellus ipsum, quis accumsan lacus vehicula nec. Fusce sapien nisi sit amet tristique accumsan. Curabitur sollicitudin, nisi sit amet consequat laoreet, erat est sollicitudin mauris, et tincidunt lorem tellus quis turpis. Sed a augue commodo, mollis leo ac, viverra odio. Etiam id pretium ex.</p></div></article>
</div>

<div class="abs ad-strip">
  <div class="ph" role="img" aria-label="Advertisement for a home warranty service" style="background:linear-gradient(180deg,#e8dcc4,#a3855c)"></div>
  <div class="ph" role="img" aria-label="Advertisement for a heritage festival" style="background:linear-gradient(180deg,#1f3f7a,#0d1f44)"></div>
  <div class="ph" role="img" aria-label="Advertisement for a local diner" style="background:linear-gradient(180deg,#f0a24a,#b85a1e)"></div>
  <div class="ph" role="img" aria-label="Advertisement for a restaurant" style="background:linear-gradient(180deg,#9b2a1f,#4c120c)"></div>
  <div class="ph" role="img" aria-label="Advertisement for a book release" style="background:linear-gradient(180deg,#d6a35a,#6a4a22)"></div>
</div>

<h2 class="abs section-title" style="top:2166px">Local Headline<span class="arrows">‹›</span></h2>
<div class="abs cards" style="top:2222px">
  <div class="card"><div class="ph" role="img" aria-label="Photo of a man working at a laptop" style="background:linear-gradient(135deg,#dfe3e6,#8c979e);height:160px"></div><h4>Sed faucibus est maximus eros congue</h4><p>Mauris sagittis in erat et facilisi. Cras et risus efficitur.</p></div>
  <div class="card"><div class="ph" role="img" aria-label="Photo of a market chart on a screen" style="background:linear-gradient(135deg,#3d4a45,#121816);height:160px"></div><h4>Magna vitae consequat dapibus</h4><p>Mauris sagittis in erat et facilisi. Cras et risus efficitur.</p></div>
  <div class="card"><div class="ph" role="img" aria-label="Photo of a glowing light display" style="background:linear-gradient(135deg,#f3c26b,#7a3d2a 60%,#2a1a18);height:160px"></div><h4>Sed faucibus est maximus eros congue</h4><p>Mauris sagittis in erat et facilisi. Cras et risus efficitur.</p></div>
  <div class="card"><div class="ph" role="img" aria-label="Photo of colleagues at a meeting" style="background:linear-gradient(135deg,#d4d9dc,#6d7880);height:160px"></div><h4>Sed faucibus est maximus eros congue</h4><p>Mauris sagittis in erat et facilisi. Cras et risus efficitur.</p></div>
</div>

<div class="abs side ph" style="top:176px;height:300px;background:linear-gradient(180deg,#7a5a3a,#d9792a 60%,#4f3a22)" role="img" aria-label="Advertisement with autumn pumpkins display"></div>
<div class="abs side ph" style="top:490px;height:330px;background:linear-gradient(180deg,#e6d94a,#6f9a3a 60%,#3f5a24)" role="img" aria-label="Advertisement for a local magazine cover"></div>
<div class="abs side ph" style="top:860px;height:340px;background:linear-gradient(180deg,#7c9a4a,#3e5a2a)" role="img" aria-label="Advertisement featuring a wildlife photograph"></div>
<div class="abs side ph" style="top:1220px;height:320px;background:linear-gradient(180deg,#0c0c14,#3a1a3a 50%,#0a0a10)" role="img" aria-label="Advertisement for a county fireworks show"></div>
<div class="abs newsletter">
  <h4>NEWSLETTER</h4>
  <p>Join the cedar lantern gazette list and get daily local headlines and photos in your inbox.</p>
  <div class="nl-form"><span></span><b></b></div>
</div>
<div class="abs side ph" style="top:1790px;height:370px;background:linear-gradient(180deg,#3f7a2a,#1f4a18)" role="img" aria-label="Advertisement with green garden plants"></div>
<div class="abs side ph" style="top:2180px;height:340px;background:linear-gradient(180deg,#3aa0d8,#1c6aa6)" role="img" aria-label="Advertisement for Harvest Valley Dairy Days"></div>

<footer class="abs footer">
  <div class="foot-cols">
    <ul><li>Terms of Use</li><li>About Cedar Lantern Gazette</li><li>Privacy Policy</li><li>Cookies</li></ul>
    <ul><li>Accessibility Help</li><li>Parental Guidance</li><li>Contact Cedar Lantern Gazette</li></ul>
    <ul><li>Login</li><li>Signup</li><li>News</li></ul>
    <ul class="foot-social"><li><i></i>Friendloop</li><li><i></i>Chirpwave</li><li><i></i>Orbitshare</li><li><i></i>RSS</li></ul>
  </div>
  <div class="copy">Copyright 2024 | CedarLanternGazette</div>
</footer>

</body>
</html>
```